Quill Refrigeration. Refrigeration and air conditioning specialists.

We need a website to promote our business. We would a modern simple design using the colours from our logo and black. We want it to be fun but proffesional.

Target Market(s)

Commercial

Number of Pages Required

4 page

Requirements
Must have
• Home Page, About Us, Services and Contact Us.
• 24/7 365 days service available.
• Quill Refrigeration's dedicated team specialises in commercial refrigeration and air conditioning equipment.
• Based in Joondalup, we cover Perth Metro and surrounding areas.
Nice to have
• KNOWLEDGE . EXPERIENCE . PASSION in bold.
• Our experienced and highly trained technicians provide extensive knowledge and exceptional skills for your commercial refrigeration and air conditioning requirements.
• Pictures of commercial refrigeration.
Should not have
• No mention of domestic services.

```html
<!DOCTYPE html>
<html lang="en">
<head>
<meta charset="utf-8">
<title>Quill Refrigeration</title>
<link href="https://fonts.googleapis.com/css2?family=Raleway:wght@400;500;600;700;800&display=swap" rel="stylesheet">
<style>
:root{
  --lime:#a4f46b;
  --lime-text:#8ee878;
  --ink:#151515;
  --body:#222;
  --muted:#666;
  --page:#f6f7fb;
  --card-border:#d9dbe2;
  --footer:#5b5b5b;
  --field:#d6d8de;
  --dot:#7a7790;
}
*{box-sizing:border-box;margin:0;padding:0}
html,body{width:1200px;height:2752px;overflow:hidden}
body{position:relative;background:var(--page);font-family:'Raleway',sans-serif;color:var(--body)}
.abs{position:absolute}

/* header */
.site-header{left:0;top:0;width:1200px;height:120px;background:var(--page)}
.brand{left:152px;top:28px;display:flex;align-items:center;gap:10px}
.brand-mark{width:22px;height:22px;background:var(--lime)}
.brand-name{font-weight:800;font-size:30px;color:var(--lime);letter-spacing:.5px}
.main-nav{left:608px;top:46px;display:flex;gap:37px;font-size:20px;color:#444}

/* hero */
.hero{left:0;top:120px}
.hero-title{left:150px;top:256px;font-weight:700;font-size:44px;line-height:53px;color:#fff;letter-spacing:.5px}
.hero-title .accent{color:var(--lime)}
.btn-book{left:228px;top:428px;width:136px;height:36px;border:2px solid var(--lime);color:#fff;font-size:11px;font-weight:700;display:flex;align-items:center;justify-content:center;letter-spacing:.5px}

/* intro */
.intro-title{left:0;top:634px;width:1200px;text-align:center;font-size:20px;font-weight:500;color:var(--body)}
.intro-text{left:290px;top:682px;width:620px;text-align:center;font-size:10.5px;line-height:16px;color:var(--muted)}
.feature-card{top:763px;width:277px;height:192px;background:#fff;border:1px solid var(--card-border);text-align:center;padding-top:30px}
.feature-card svg{display:block;margin:0 auto}
.feature-card h3{font-size:15px;font-weight:500;margin-top:18px;color:var(--body)}
.feature-card p{font-size:10.5px;line-height:16px;color:var(--muted);margin:14px auto 0;width:220px}
.team-heading{left:0;top:1026px;width:1200px;text-align:center;font-size:18px;font-weight:700;letter-spacing:1.4px;line-height:32px;color:var(--ink)}

/* gallery */
.gallery-photo{height:343px}
.load-more{left:0;top:1876px;width:1200px;text-align:center;font-size:12px;font-weight:700;letter-spacing:.5px;color:var(--ink)}
.pager{left:566px;top:1900px;display:flex;gap:13px}
.pager span{width:13px;height:13px;border-radius:50%;background:var(--dot)}

/* contact */
.contact{left:0;top:1958px;width:1200px;height:528px;background:linear-gradient(180deg,#2b2f35 0%,#3a3f44 55%,#2a2c2e 100%)}
.contact-title{left:0;top:2006px;width:1200px;text-align:center;color:#fff;font-size:18px;font-weight:600}
.form-note{left:157px;top:2074px;width:310px;font-size:9.5px;line-height:15px;color:var(--lime-text)}
.field{background:var(--field);font-size:9.5px;color:#444;padding:9px 10px}
.btn-send{left:376px;top:2382px;width:136px;height:42px;background:var(--lime);color:var(--ink);font-size:11px;font-weight:700;display:flex;align-items:center;justify-content:center}
.contact-info{left:650px;top:2112px;color:var(--lime-text);font-size:23px;font-weight:500;letter-spacing:.5px}
.info-row{position:absolute;left:0;display:flex;align-items:flex-start;gap:30px;white-space:nowrap}
.info-row svg{flex:none}

/* footer */
.site-footer{left:0;top:2488px;width:1200px;height:264px;background:var(--footer);color:#fff}
.footer-brand{left:212px;top:2530px;display:flex;align-items:center;gap:8px}
.footer-brand .brand-mark{width:16px;height:16px;background:#fff}
.footer-brand .brand-name{font-size:22px;color:#fff}
.footer-about{left:212px;top:2580px;width:228px;font-size:9.5px;line-height:12px;color:#fff}
.follow{left:210px;top:2642px;font-size:15px}
.socials{left:220px;top:2670px;display:flex;gap:6px}
.socials span{width:19px;height:19px;background:#fff;border-radius:3px}
.footer-links{font-size:15px;line-height:31px}
.footer-links a{display:block;color:#fff;text-decoration:none}
</style>
</head>
<body>

<header class="site-header abs">
  <div class="brand abs"><span class="brand-mark"></span><span class="brand-name">Quill</span></div>
  <nav class="main-nav abs"><span>Home</span><span>About Us</span><span>Services</span><span>Conact Us</span></nav>
</header>

<svg class="hero abs" width="1200" height="458" viewBox="0 0 1200 458">
  <defs>
    <linearGradient id="heroPhoto" x1="0" y1="0" x2="1" y2="1">
      <stop offset="0" stop-color="#8d97a3"/>
      <stop offset=".5" stop-color="#c9cfd5"/>
      <stop offset=".75" stop-color="#e36a2a"/>
      <stop offset="1" stop-color="#7d5c48"/>
    </linearGradient>
  </defs>
  <rect width="1200" height="458" fill="url(#heroPhoto)" role="img" aria-label="Technician in hard hat and hi-vis jacket servicing a rooftop air conditioning unit"/>
  <polygon points="0,0 470,0 712,405 0,405" fill="#0c0c0c" opacity=".94"/>
  <rect x="0" y="405" width="720" height="53" fill="#2a2a2a"/>
  <polygon points="712,405 1200,395 1200,458 742,458" fill="var(--lime)"/>
</svg>
<h1 class="hero-title abs">KNOWLEDGE.<br><span class="accent">EXPERIENCE.</span><br>PASSION.</h1>
<div class="btn-book abs">BOOK NOW</div>

<h2 class="intro-title abs">Most Trusted Commercial Refrigeration &amp; AC Specialists</h2>
<p class="intro-text abs">Our experienced and highly trained technicians provide extensive knowledge and exceptional skills for your commercial refrigeration and air conditioning requirements.</p>

<div class="feature-card abs" style="left:150px">
  <svg width="38" height="38" viewBox="0 0 38 38" fill="none" stroke="#333" stroke-width="2"><path d="M32 12A15 15 0 1 1 22 4.5"/><path d="M19 10v10l6 4"/><path d="M22 1l1 4-4 1"/></svg>
  <h3>Open 24/7 - Available</h3>
  <p>Emergency repair services 24 hours a day, seven days a week. Quill all time ready to repair &amp; supportive.</p>
</div>
<div class="feature-card abs" style="left:456px">
  <svg width="38" height="38" viewBox="0 0 38 38" fill="none" stroke="#333" stroke-width="2"><path d="M19 33L6 20a8 8 0 0 1 13-10 8 8 0 0 1 13 10z"/></svg>
  <h3>Satisfaction Guaranteed</h3>
  <p>Quill Service offers 100% satisfaction guarantees on all Air-conditioner &amp; Heating services.</p>
</div>
<div class="feature-card abs" style="left:771px">
  <svg width="38" height="38" viewBox="0 0 38 38" fill="none" stroke="#333" stroke-width="2"><circle cx="19" cy="19" r="16"/><circle cx="19" cy="15" r="6"/><path d="M9 30c3-6 17-6 20 0"/></svg>
  <h3>Professional Technicians</h3>
  <p>Our technicians have your safety, welfare and comfort in mind at all times, they are certified and experienced.</p>
</div>

<h2 class="team-heading abs">QUILL REFRIGERATION'S DEDICATED TEAM SPECIALISES IN COMMERCIAL REFRIGERATION<br>AND AIR CONDITIONING EQUIPMENT.</h2>

<div class="gallery-photo abs" style="left:0;top:1155px;width:401px;background:linear-gradient(135deg,#c8ccd0,#3c4a66)" role="img" aria-label="Technician checking gauges on a commercial condensing unit"></div>
<div class="gallery-photo abs" style="left:403px;top:1155px;width:397px;background:linear-gradient(135deg,#6b6259,#c95a3c)" role="img" aria-label="Hands wiring the control panel of a refrigeration unit"></div>
<div class="gallery-photo abs" style="left:802px;top:1155px;width:398px;background:linear-gradient(135deg,#d9d7d2,#5a4f60 70%,#e0602a)" role="img" aria-label="Pressure gauge and wrench on refrigerant pipework"></div>
<div class="gallery-photo abs" style="left:0;top:1502px;width:401px;background:linear-gradient(135deg,#8a7866,#e2c23a 55%,#3a3b44)" role="img" aria-label="Two technicians in hard hats inspecting an electrical panel"></div>
<div class="gallery-photo abs" style="left:403px;top:1502px;width:397px;background:linear-gradient(135deg,#9ea4ab,#3c3f45 60%,#c7d23a)" role="img" aria-label="Technician in blue hard hat working on an air conditioning unit"></div>
<div class="gallery-photo abs" style="left:802px;top:1502px;width:398px;background:linear-gradient(135deg,#e9e9e6,#4a6b9a 65%,#303238)" role="img" aria-label="Technician testing a commercial refrigeration compressor with a meter"></div>

<div class="load-more abs">LOAD MORE</div>
<div class="pager abs"><span></span><span></span><span></span></div>

<section class="contact abs" role="img" aria-label="Darkened city skyline behind the booking form"></section>
<h2 class="contact-title abs">Book for a visit Now!</h2>
<p class="form-note abs">To request an appointment with Daniel, please provide your contact information by filling out the form below</p>
<div class="field abs" style="left:155px;top:2129px;width:170px;height:28px">Your Name</div>
<div class="field abs" style="left:352px;top:2129px;width:161px;height:28px">Phone</div>
<div class="field abs" style="left:155px;top:2189px;width:170px;height:30px">Your Email</div>
<div class="field abs" style="left:352px;top:2189px;width:161px;height:30px">Date &nbsp;&nbsp;___ / ___ / ___</div>
<div class="field abs" style="left:155px;top:2248px;width:358px;height:106px">Message</div>
<div class="btn-send abs">Send Message</div>

<div class="contact-info abs">
  <div class="info-row" style="top:0">
    <svg width="24" height="30" viewBox="0 0 24 30"><path d="M12 0a11 11 0 0 0-11 11c0 8 11 19 11 19s11-11 11-19A11 11 0 0 0 12 0z" fill="var(--lime)"/></svg>
    <div style="line-height:46px;margin-top:-10px">27 HARBOUR LANE<br>JONDALUP<br>PERTH METRO 6027</div>
  </div>
  <div class="info-row" style="top:170px">
    <svg width="24" height="26" viewBox="0 0 24 26" fill="none" stroke="var(--lime)" stroke-width="2.4"><path d="M5 2l5 6-3 3c2 4 5 7 9 9l3-3 5 5-3 3C10 24 1 15 2 5z"/></svg>
    <div>555-014-2290</div>
  </div>
  <div class="info-row" style="top:224px">
    <svg width="26" height="20" viewBox="0 0 26 20"><rect width="26" height="20" fill="var(--lime)"/><path d="M1 2l12 9 12-9" fill="none" stroke="#333" stroke-width="2"/></svg>
    <div>hello@quillcooling.example</div>
  </div>
</div>

<footer class="site-footer abs"></footer>
<div class="footer-brand abs"><span class="brand-mark"></span><span class="brand-name">Quill</span></div>
<p class="footer-about abs">Lorem ipsum dolor sit amet, consectetur adipiscing elit, sed do eiusmod tempor incididunt ut labore et dolore magna aliqua. Ut enim ad minim veniam, quis nostrud exercitation ullamco laboris nisi ut</p>
<div class="follow abs">Follow Us On</div>
<div class="socials abs"><span></span><span></span><span></span></div>
<nav class="footer-links abs" style="left:592px;top:2535px"><a>Home</a><a>About Us</a><a>Services</a><a>Contact Us</a></nav>
<nav class="footer-links abs" style="left:818px;top:2535px"><a>Terms &amp; Conditions</a><a>Privacy Policy</a><a>Terms of Use</a><a>Funding Request</a></nav>

</body>
</html>
```